Yard Sign Design for luxury design & build company

Looking to have 18" x 24" company yard signs designed.
An update to the business logo might be helpful.
Photos are not necessary but use if you can make inspiring.

Industry: Construction

Looking for a large headline of "Basement Finishing"
Website: www.tamberlyhomes.com
Phone Number (612) 555-0174
FB link: facebook.com/tamberlyhomesmn
Instagram: www.instagram.com/tamberlyhomesmn

Industry/Entity Type

Construction

Colors

Designer to choose colors to be used in the design.

Requirements
Must have
• Impactful high end characteristics
Nice to have
• Depth and detail graphis

```html
<!DOCTYPE html>
<html lang="en">
<head>
<meta charset="utf-8">
<title>Basement Finishing – Tamberly Homes Yard Sign</title>
<link rel="stylesheet" href="https://fonts.googleapis.com/css2?family=Open+Sans:wght@400;600;700;800&display=swap">
<style>
  :root {
    --sign-red: #e0261f;
    --sign-red-deep: #c81c16;
    --ink: #111111;
    --paper: #ffffff;
    --backdrop: #eeeeee;
    --star-gold: #f5b400;
    --photo-warm: #b8926a;
    --photo-light: #e6ddd2;
    --photo-dark: #5a4636;
  }
  html, body {
    margin: 0;
    padding: 0;
    width: 824px;
    height: 1200px;
    overflow: hidden;
    background: var(--backdrop);
  }
  .canvas {
    position: relative;
    width: 824px;
    height: 1200px;
  }
  .yard-sign {
    position: absolute;
    left: 22px;
    top: 308px;
    width: 780px;
    height: 584px;
    background: var(--paper);
    box-shadow: 0 6px 18px rgba(0,0,0,0.22);
  }
  .yard-sign svg { display: block; width: 100%; height: 100%; }
  .headline {
    font-family: "Open Sans", Arial, sans-serif;
    font-weight: 800;
    font-size: 168px;
  }
  .headline-top { fill: var(--paper); }
  .headline-bottom { fill: var(--ink); }
  .brand-name {
    font-family: "Open Sans", Arial, sans-serif;
    font-weight: 700;
    fill: var(--ink);
  }
  .phone-text {
    font-family: "Open Sans", Arial, sans-serif;
    font-size: 48px;
    fill: var(--paper);
  }
  .phone-area { font-weight: 400; }
  .phone-number { font-weight: 700; }
  .website {
    font-family: "Open Sans", Arial, sans-serif;
    font-size: 42px;
    fill: var(--ink);
  }
  .website-name { font-weight: 700; }
  .review-label {
    font-family: "Open Sans", Arial, sans-serif;
    font-weight: 700;
    font-size: 24px;
    fill: #333333;
  }
  .review-score {
    font-family: "Open Sans", Arial, sans-serif;
    font-weight: 800;
    font-size: 42px;
    fill: #333333;
  }
  .review-stars {
    font-family: "Open Sans", Arial, sans-serif;
    font-size: 38px;
    fill: var(--star-gold);
  }
  .social-handle {
    font-family: "Open Sans", Arial, sans-serif;
    font-weight: 400;
    font-size: 30px;
    fill: var(--ink);
  }
</style>
</head>
<body>
<main class="canvas">
  <section class="yard-sign" aria-label="Basement Finishing yard sign for Tamberly Homes">
    <svg viewBox="0 0 1436 1075" xmlns="http://www.w3.org/2000/svg">
      <defs>
        <linearGradient id="red-panel-fill" x1="0" y1="0" x2="1" y2="1">
          <stop offset="0" stop-color="#e8312a"/>
          <stop offset="1" stop-color="#d11f19"/>
        </linearGradient>
        <linearGradient id="room-lounge" x1="0" y1="0" x2="0" y2="1">
          <stop offset="0" stop-color="#ece6de"/>
          <stop offset="0.55" stop-color="#9c8472"/>
          <stop offset="1" stop-color="#6b4f3a"/>
        </linearGradient>
        <linearGradient id="room-billiards" x1="0" y1="0" x2="0" y2="1">
          <stop offset="0" stop-color="#f1ece6"/>
          <stop offset="0.5" stop-color="#b59d85"/>
          <stop offset="1" stop-color="#4f3d31"/>
        </linearGradient>
        <linearGradient id="room-bar" x1="0" y1="0" x2="0" y2="1">
          <stop offset="0" stop-color="#e3dbd1"/>
          <stop offset="0.5" stop-color="#8f6f58"/>
          <stop offset="1" stop-color="#7a5a40"/>
        </linearGradient>
      </defs>

      <!-- header swoosh -->
      <path class="swoosh-shadow" fill="var(--ink)"
        d="M0 190 C30 330 200 470 400 600 C700 800 1200 730 1436 628 V590 C1200 690 700 760 400 560 C200 430 40 300 0 190 Z"/>
      <path class="swoosh-red" fill="url(#red-panel-fill)"
        d="M0 0 H1436 V590 C1200 690 700 760 400 560 C200 430 40 300 0 190 Z"/>

      <!-- headline -->
      <text class="headline headline-top" x="182" y="197" textLength="1053" lengthAdjust="spacing">BASEMENT</text>
      <text class="headline headline-bottom" x="182" y="363" textLength="1028" lengthAdjust="spacing">FINISHING</text>

      <!-- project photo circles -->
      <circle class="project-photo" cx="400" cy="575" r="146" fill="url(#room-lounge)"
        stroke="var(--sign-red)" stroke-width="9" role="img"
        aria-label="Finished basement lounge with sectional sofa and bar"/>
      <circle class="project-photo" cx="1000" cy="580" r="150" fill="url(#room-bar)"
        stroke="var(--sign-red)" stroke-width="9" role="img"
        aria-label="Finished basement bar area with stone fireplace"/>
      <circle class="project-photo" cx="715" cy="632" r="184" fill="url(#room-billiards)"
        stroke="var(--sign-red)" stroke-width="9" role="img"
        aria-label="Finished basement game room with billiard table"/>

      <!-- brand mark -->
      <g class="brand">
        <circle cx="203" cy="862" r="58" fill="none" stroke="var(--sign-red)" stroke-width="6"/>
        <text class="brand-name" x="203" y="985" font-size="40" text-anchor="middle" textLength="226" lengthAdjust="spacing">TAMBERLY</text>
        <text class="brand-name" x="203" y="1014" font-size="20" text-anchor="middle" textLength="226" lengthAdjust="spacing">HOMES</text>
      </g>

      <!-- phone bar -->
      <g class="phone-bar">
        <rect x="447" y="898" width="553" height="75" rx="8" fill="var(--ink)"/>
        <path d="M455 898 H535 V973 H455 A8 8 0 0 1 447 965 V906 A8 8 0 0 1 455 898 Z" fill="var(--sign-red)"/>
        <path class="phone-icon" fill="var(--paper)"
          d="M478 918 c3-2 7-2 9 1 l6 9 c2 3 1 6-1 8 l-4 3 c2 6 8 13 15 16 l3-4 c2-2 5-3 8-1 l9 6 c3 2 3 6 1 9 l-4 5 c-3 3-8 4-13 2 c-14-6-26-18-32-32 c-2-5-1-10 2-13 Z"/>
        <text class="phone-text" x="556" y="952" textLength="420" lengthAdjust="spacing"><tspan class="phone-area">(612) </tspan><tspan class="phone-number">555-0174</tspan></text>
      </g>

      <!-- website -->
      <text class="website" x="447" y="1026" textLength="553" lengthAdjust="spacing">www.<tspan class="website-name">tamberlyhomes</tspan>.com</text>

      <!-- review badge -->
      <g class="review-badge">
        <circle cx="1142" cy="903" r="26" fill="#d9d9d9"/>
        <text class="review-label" x="1180" y="900">Verified</text>
        <text class="review-label" x="1180" y="925">Client Reviews</text>
        <text class="review-score" x="1110" y="966">5.0</text>
        <text class="review-stars" x="1180" y="964" letter-spacing="2">★★★★★</text>
      </g>

      <!-- social handle -->
      <g class="social">
        <circle cx="1124" cy="1017" r="15" fill="var(--sign-red)"/>
        <text class="social-handle" x="1150" y="1027">tamberlyhomes</text>
      </g>
    </svg>
  </section>
</main>
</body>
</html>
```